Escrow Accounting firm needs a website design for a startup that services clients nationally.

I offer escrow accounting services for title companies and real estate attorneys. I've enclosed a logo, color palette and flyers with content that can be used for the site.

I'm looking for a similar design concept as the website below from my former employer. Please don't copy because of copyright infringement. Including for design ideas only.
www.harborlinefiduciary.com

Below is a brief write-up...
For professionals in the title insurance industry, finding a trustworthy and budget-friendly solution for escrow accounting can be daunting. When choosing the right accounting partner, title companies and law firms need a group they can rely on, and that's where we come in.

```html
<!DOCTYPE html>
<html lang="en">
<head>
<meta charset="utf-8">
<title>Meridian Escrow Solutions</title>
<link rel="stylesheet" href="https://fonts.googleapis.com/css2?family=Domine:wght@500;700&family=Open+Sans:wght@400;600;700&display=swap">
<style>
:root{
  --navy:#363f4f;
  --navy-deep:#2f3644;
  --clay:#b97561;
  --clay-dark:#b06c57;
  --ink:#3a3a3a;
  --muted:#6b6b6b;
  --line:#e6e6e6;
  --white:#ffffff;
}
*{box-sizing:border-box;margin:0;padding:0}
html,body{width:1200px;height:2508px;overflow:hidden;background:var(--white)}
body{position:relative;font-family:"Open Sans",sans-serif;color:var(--ink)}
.abs{position:absolute}
.serif{font-family:"Domine",serif}
.eyebrow{font-size:12px;color:var(--clay);text-transform:uppercase;letter-spacing:.3px}
.btn{position:absolute;background:var(--clay);color:var(--white);font-size:10px;font-weight:700;letter-spacing:.5px;display:flex;align-items:center;justify-content:center;text-transform:uppercase}

/* top bar */
.brand{left:220px;top:14px;display:flex;align-items:center;gap:8px}
.brand-mark{width:26px;height:26px;background:var(--clay)}
.brand-name{font-size:20px;font-weight:600;color:var(--clay);line-height:1}
.brand-name small{display:block;font-size:9px;font-weight:600;color:var(--clay);letter-spacing:.5px;margin-top:2px}
.info{top:14px;display:flex;gap:10px;font-size:9px;line-height:14px;color:var(--ink)}
.info svg{margin-top:4px}
.topline{left:0;top:55px;width:1200px;height:1px;background:var(--line)}
.nav{left:224px;top:67px;display:flex;gap:36px;font-size:10px;letter-spacing:.4px;color:var(--ink)}
.quote{left:871px;top:56px;width:151px;height:38px}

/* hero */
.hero{left:0;top:94px;width:1200px;height:492px;background:linear-gradient(100deg,#3a342f 0%,#4e4540 45%,#3d3631 70%,#2c2724 100%)}
.hero h1{left:214px;top:127px;font-size:36px;line-height:46px;color:var(--white);font-weight:700;letter-spacing:.5px}
.hero .sub{left:212px;top:225px;font-size:17px;color:#d2876f;text-transform:uppercase;letter-spacing:.2px}
.hero p{left:213px;top:254px;width:480px;font-size:9.5px;line-height:15px;color:#e9e4e1}
.hero .btn{left:213px;top:329px;width:151px;height:38px}

/* service cards */
.card{top:557px;height:287px;padding:0 48px}
.card h3{position:absolute;left:48px;top:95px;font-size:16px;line-height:21px;font-weight:700;letter-spacing:.3px}
.card p{position:absolute;left:41px;top:160px;width:300px;font-size:9.5px;line-height:15.2px}
.card .arrow{position:absolute;right:28px;bottom:14px}
.card .icon{position:absolute;left:55px;top:32px}
.c1{left:7px;width:388px;background:var(--navy);color:var(--white)}
.c2{left:405px;width:386px;background:var(--clay);color:var(--white)}
.c3{left:800px;width:390px;background:var(--white);color:var(--ink);box-shadow:0 4px 10px rgba(0,0,0,.12)}
.c1,.c2{box-shadow:0 4px 10px rgba(0,0,0,.15)}

/* about */
.about-frame{left:205px;top:889px;width:344px;height:313px;background:var(--navy)}
.about-corner{left:512px;top:1245px;width:60px;height:60px;background:var(--navy)}
.about-photo{left:253px;top:918px;width:306px;height:377px;background:linear-gradient(160deg,#c9c6c2 0%,#a9a49e 45%,#e8e6e2 100%)}
.exp{left:453px;top:1042px;width:125px;height:118px;background:var(--white);box-shadow:0 3px 10px rgba(0,0,0,.18);text-align:center}
.exp b{display:block;font-family:"Domine",serif;font-size:32px;color:var(--navy);margin-top:22px}
.exp span{font-size:9px;color:var(--muted)}
.about-eye{left:619px;top:962px}
.about-title{left:617px;top:985px;font-size:22px;line-height:29px;color:var(--navy);font-weight:700;letter-spacing:.4px}
.about-text{left:604px;top:1054px;width:410px;font-size:9.5px;line-height:15.2px;color:var(--muted)}
.about-btn{left:601px;top:1165px;width:151px;height:38px}

/* why */
.why{left:0;top:1346px;width:577px;height:332px;background:var(--navy)}
.why-photo{left:577px;top:1346px;width:623px;height:332px;background:linear-gradient(110deg,#ececec 0%,#d9dbe2 40%,#a7876c 70%,#2a2421 100%)}
.why-eye{left:213px;top:1418px}
.why h2{left:211px;top:1436px;font-size:22px;color:var(--white);font-weight:700;letter-spacing:.4px}
.why p{left:197px;top:1486px;width:340px;font-size:9.5px;line-height:15.2px;color:#e4e6ea}
.why .btn{left:197px;top:1570px;width:151px;height:38px}

/* contact */
.ct-eye{left:223px;top:1742px}
.ct-title{left:221px;top:1763px;font-size:22px;color:var(--navy);font-weight:700;letter-spacing:.5px}
.ct-text{left:207px;top:1808px;width:390px;font-size:9.5px;line-height:15.2px;color:var(--muted)}
.ct-row{left:209px;display:flex;align-items:center;gap:14px;font-size:9.5px;color:var(--muted)}
.field{border-bottom:1px solid var(--line);height:22px;display:flex;align-items:center;gap:7px;font-size:7.5px;color:var(--muted)}
.send{left:673px;top:1920px;width:94px;height:27px;background:var(--clay);color:var(--white);display:flex;align-items:center;justify-content:center;gap:8px;font-size:12px;font-weight:600}
.agree{left:787px;top:1930px;font-size:6.5px;color:var(--muted);display:flex;gap:5px;align-items:center}
.agree i{width:7px;height:7px;border:1px solid #999;display:inline-block}
.agree u{color:var(--ink)}

/* map */
.map{left:0;top:2003px;width:1200px;height:167px;background:linear-gradient(90deg,#d8ead6 0%,#e8ece8 30%,#a9c9ef 47%,#aecbf0 53%,#eceae6 70%,#ede6dc 100%)}

/* footer */
.footer{left:0;top:2170px;width:1200px;height:296px;background:var(--navy)}
.f-brand{left:208px;top:2256px;display:flex;align-items:center;gap:10px}
.f-brand .brand-mark{width:34px;height:34px;background:var(--white)}
.f-brand .brand-name{color:var(--white);font-size:24px}
.f-brand .brand-name small{color:var(--white);font-size:11px}
.f-text{left:212px;top:2317px;width:220px;font-size:9.5px;line-height:15.2px;color:var(--white)}
.f-social{left:212px;top:2362px;display:flex;gap:9px}
.f-social i{width:16px;height:16px;border:1px solid var(--white);border-radius:50%;display:block}
.f-col{font-size:9.5px;line-height:15.2px;color:var(--white)}
.f-col h4{font-size:11.5px;font-weight:600;letter-spacing:.3px;margin-bottom:14px}
.copy{left:0;top:2466px;width:1200px;height:42px;background:var(--clay-dark);color:var(--white);font-size:9.5px;padding:19px 0 0 208px}
</style>
</head>
<body>

<header>
  <div class="abs brand">
    <span class="brand-mark"></span>
    <span class="brand-name">MERIDIAN<small>ESCROW SOLUTIONS</small></span>
  </div>
  <div class="abs info" style="left:549px">
    <svg width="14" height="14" viewBox="0 0 24 24" fill="none" stroke="#555" stroke-width="1.6"><path d="M5 3h4l2 5-3 2a11 11 0 0 0 6 6l2-3 5 2v4a2 2 0 0 1-2 2A17 17 0 0 1 3 5a2 2 0 0 1 2-2z"/></svg>
    <div>Phone number:<br>(415) 555-0147</div>
  </div>
  <div class="abs info" style="left:684px">
    <svg width="14" height="14" viewBox="0 0 24 24" fill="none" stroke="#555" stroke-width="1.6"><circle cx="12" cy="12" r="9"/><path d="M12 7v5l3 2"/></svg>
    <div>hello@meridianescrow.com<br>Visit Us: 8.00 AM - 6.00 PM</div>
  </div>
  <div class="abs info" style="left:851px;top:16px">
    <svg width="14" height="14" viewBox="0 0 24 24" fill="none" stroke="#555" stroke-width="1.6"><path d="M12 21s-7-6-7-12a7 7 0 0 1 14 0c0 6-7 12-7 12z"/><circle cx="12" cy="9" r="2.5"/></svg>
    <div>Address Center<br>2450 Harbor Way, Oakland, CA 946</div>
  </div>
  <div class="abs topline"></div>
  <nav class="abs nav"><span>HOME</span><span>ABOUT US</span><span>OUR SERVICES</span><span>CONTACT US</span></nav>
  <div class="btn quote">Request a quote</div>
</header>

<section class="abs hero" role="img" aria-label="Photo of three accounting professionals reviewing documents together"></section>
<h1 class="abs serif hero-h" style="left:214px;top:221px;font-size:36px;line-height:46px;color:#fff;font-weight:700;letter-spacing:.5px">Trusted Escrow<br>Accounting Solutions</h1>
<div class="abs" style="left:212px;top:318px;font-size:17px;color:#d2876f;letter-spacing:.2px">FOR TITLE COMPANIES AND REAL ESTATE ATTORNEYS</div>
<p class="abs" style="left:213px;top:347px;width:480px;font-size:9.5px;line-height:15px;color:#e9e4e1">Navigating the complexities of escrow accounting in the title insurance industry requires precision, reliability, and trust. Our dedicated team specializes in providing cost-effective and dependable escrow accounting services tailored for title companies and real estate attorneys.</p>
<div class="btn" style="left:213px;top:423px;width:151px;height:38px">Learn more</div>
<svg class="abs" style="left:20px;top:304px" width="22" height="36" viewBox="0 0 22 36" fill="none" stroke="#fff" stroke-width="2"><path d="M18 2L4 18l14 16"/></svg>
<svg class="abs" style="left:1160px;top:304px" width="22" height="36" viewBox="0 0 22 36" fill="none" stroke="#fff" stroke-width="2"><path d="M4 2l14 16L4 34"/></svg>

<section>
  <article class="abs card c1">
    <svg class="icon" width="56" height="50" viewBox="0 0 56 50"><rect x="0" y="4" width="22" height="30" fill="#b97561"/><rect x="8" y="0" width="26" height="36" fill="none" stroke="#fff" stroke-width="1.5"/><path d="M22 10h8M22 16h8M14 26h14M14 31h10" stroke="#fff" stroke-width="1.5"/><text x="11" y="18" fill="#fff" font-size="11" font-family="Open Sans">$</text><circle cx="38" cy="36" r="7" fill="none" stroke="#fff" stroke-width="1.5"/><path d="M35 36l2 2 4-4" stroke="#fff" stroke-width="1.5" fill="none"/></svg>
    <h3 class="serif">Escrow Reconciliation<br>Services</h3>
    <p>Accurate and timely reconciliation is critical in managing escrow accounts. Our Escrow Reconciliation Services ensure that all transactions are thoroughly reviewed and balanced, helping you maintain compliance and avoid costly errors. We provide detailed reports and insights to keep your financials in check and your business running smoothly.</p>
    <svg class="arrow" width="20" height="10" viewBox="0 0 20 10" fill="none" stroke="#fff" stroke-width="1.4"><path d="M0 5h18M14 1l4 4-4 4"/></svg>
  </article>
  <article class="abs card c2">
    <svg class="icon" width="60" height="46" viewBox="0 0 60 46"><rect x="0" y="2" width="24" height="32" fill="#fff"/><path d="M14 10l16 4 16-4v30l-16 4-16-4z" fill="none" stroke="#2f3644" stroke-width="1.5"/><path d="M30 14v30M18 18l8 2M18 24l8 2M34 20l8-2M34 26l8-2" stroke="#2f3644" stroke-width="1.3"/></svg>
    <h3 class="serif">Best Practices<br>Certification</h3>
    <p>Stay ahead in the industry with our Best Practices Certification service. We help title companies and real estate attorneys adhere to industry standards by providing rigorous evaluations and certifications. This service not only ensures compliance but also enhances your credibility with clients and partners.</p>
    <svg class="arrow" width="20" height="10" viewBox="0 0 20 10" fill="none" stroke="#fff" stroke-width="1.4"><path d="M0 5h18M14 1l4 4-4 4"/></svg>
  </article>
  <article class="abs card c3">
    <svg class="icon" style="left:50px" width="56" height="50" viewBox="0 0 56 50"><rect x="0" y="2" width="24" height="26" fill="#b97561"/><circle cx="33" cy="22" r="6" fill="#fff" stroke="#2f3644" stroke-width="1.5"/><path d="M22 44c0-8 5-12 11-12s11 4 11 12z" fill="#fff" stroke="#2f3644" stroke-width="1.5"/><path d="M20 6l2 4 4 .5-3 3 1 4-4-2-4 2 1-4-3-3 4-.5zM36 4l1.5 3 3 .4-2 2 .5 3-3-1.5-3 1.5.5-3-2-2 3-.4zM50 6l1.5 3 3 .4-2 2 .5 3-3-1.5-3 1.5.5-3-2-2 3-.4z" fill="none" stroke="#2f3644" stroke-width="1.2"/></svg>
    <h3 class="serif" style="left:63px;top:91px;color:#363f4f">Customized Review<br>Services</h3>
    <p style="left:57px;top:158px;color:#6b6b6b">Every business has unique needs, and our Customized Review Services are designed to address them. Whether you require a one-time audit or ongoing support, we tailor our review services to match your specific requirements. Our experts provide thorough and insightful analyses, helping you optimize your escrow processes and safeguard your financial health.</p>
    <svg class="arrow" width="20" height="10" viewBox="0 0 20 10" fill="none" stroke="#b97561" stroke-width="1.4"><path d="M0 5h18M14 1l4 4-4 4"/></svg>
  </article>
</section>

<section>
  <div class="abs about-frame"></div>
  <div class="abs about-corner"></div>
  <div class="abs about-photo" role="img" aria-label="Portrait of the firm's founder seated on stone steps"></div>
  <div class="abs exp"><b>15</b><span>Years of experience</span></div>
  <div class="abs eyebrow about-eye">About us?</div>
  <h2 class="abs serif about-title">Your Reliable Partner<br>in Escrow Accounting</h2>
  <p class="abs about-text">Choosing the right escrow accounting partner is crucial for ensuring your business operates smoothly and efficiently. We understand the unique challenges faced by title companies and real estate attorneys, and we're here to provide tailored solutions that meet your needs. With our expertise, attention to detail, and commitment to client satisfaction, you can trust us to manage your escrow accounting with precision and professionalism.</p>
  <div class="btn about-btn">About us</div>
</section>

<section>
  <div class="abs why"></div>
  <div class="abs why-photo" role="img" aria-label="Photo of two colleagues working together at a desk"></div>
  <div class="abs eyebrow why-eye">Why us</div>
  <h2 class="abs serif" style="left:211px;top:1436px;font-size:22px;color:#fff;font-weight:700;letter-spacing:.4px">Why choose us?</h2>
  <p class="abs" style="left:197px;top:1486px;width:340px;font-size:9.5px;line-height:15.2px;color:#e4e6ea">We recognize the distinct challenges faced by title companies and real estate attorneys, and we are dedicated to offering customized solutions that address your specific needs. With our deep expertise, meticulous attention to detail, and unwavering commitment to client</p>
  <div class="btn" style="left:197px;top:1570px;width:151px;height:38px">Services</div>
</section>

<section>
  <div class="abs eyebrow ct-eye">Contact us</div>
  <h2 class="abs serif ct-title">Get in touch !</h2>
  <p class="abs ct-text">Reach out to us today, and let's discuss how our specialized services can support your business needs. We're here to provide the solutions you need to succeed.</p>
  <div class="abs ct-row" style="top:1861px"><svg width="12" height="14" viewBox="0 0 24 28" fill="#363f4f"><path d="M12 0a10 10 0 0 0-10 10c0 8 10 18 10 18s10-10 10-18A10 10 0 0 0 12 0zm0 14a4 4 0 1 1 0-8 4 4 0 0 1 0 8z"/></svg>88 Orchard Lane, Springfield, OR 97477 US.</div>
  <div class="abs ct-row" style="top:1887px"><svg width="16" height="13" viewBox="0 0 24 24" fill="#363f4f"><path d="M5 2h4l2 5-3 2a11 11 0 0 0 6 6l2-3 5 2v4a2 2 0 0 1-2 2A17 17 0 0 1 3 4a2 2 0 0 1 2-2z"/></svg>(415) 555-0147</div>
  <div class="abs ct-row" style="top:1911px"><svg width="17" height="12" viewBox="0 0 24 16" fill="#363f4f"><path d="M0 0h24v16H0z"/><path d="M0 0l12 9 12-9" stroke="#fff" stroke-width="1.5" fill="none"/></svg>info@meridianescrow.com</div>

  <div class="abs field" style="left:675px;top:1763px;width:146px">&#9786; Name</div>
  <div class="abs field" style="left:834px;top:1763px;width:146px">&#9993; Email Address</div>
  <div class="abs field" style="left:675px;top:1805px;width:146px">&#9742; Phone</div>
  <div class="abs field" style="left:834px;top:1805px;width:146px">&#9432; Subject</div>
  <div class="abs field" style="left:675px;top:1847px;width:305px;height:46px;align-items:flex-start;padding-top:6px">&#9998; How can we help you? Feel free to get in touch!</div>
  <div class="abs send"><svg width="16" height="14" viewBox="0 0 24 22" fill="none" stroke="#fff" stroke-width="1.6"><path d="M1 9L23 1l-6 20-5-8z M12 13L23 1"/></svg>Send</div>
  <div class="abs agree"><i></i>I agree that my data is <u>collected and stored</u></div>
</section>

<div class="abs map" role="img" aria-label="Street map showing the office location by the river"></div>

<footer>
  <div class="abs footer"></div>
  <div class="abs f-brand"><span class="brand-mark"></span><span class="brand-name">MERIDIAN<small>ESCROW SOLUTIONS</small></span></div>
  <p class="abs f-text">Reach out to us today, and let's discuss how our specialized services!</p>
  <div class="abs f-social"><i></i><i></i></div>
  <div class="abs f-col" style="left:455px;top:2285px"><h4>NAVIGATION</h4>Home<br>About Us<br>Our Services<br>Contact Us</div>
  <div class="abs f-col" style="left:595px;top:2285px"><h4>SERVICES</h4>Escrow Reconciliation Services<br>Best Practices Certification<br>Customized Review Services</div>
  <div class="abs copy">Meridian Escrow Solutions &copy; 2024. All Rights Reserved.</div>
</footer>

</body>
</html>
```